New Signage Design Project for Qr Lake Facades *

Im Looking for yard design with our logo, number, website, services & credentials. Each Yard sign will be for 3 different titles...

Example 1: New Roof Coming Soon (Title) This Yardsign is for projects before we start them... Letting neighbors know why we are going to be there.
Example 2: New Roof In progress (Title) This Yardsign is for during the process of the work.. letting neighbors know what we working on!!
Example 3: This Design is only for the customer that says a title NEW ROOF INSTALL SATISFIED CUSTOMER ON THIS DESIGN I DONT NEED SERVICES JSUT LOGO AND THE TITLE

Target Market(s)

Customers

Industry/Entity Type

Roofing

Font styles to use
Serif
Sans Serif

Colors
33b8a4
5c5c5c

Requirements
Must have
• -LOGO
• -WEBSITE
• -NUMBER
• -TITLES
• -SERVICES (ROOFING, GUTTERS, PAINTING, PRESSURE WASHING, EXTERIOR DESIGN.)
• -CREDENTIALS
• -HOUSE SHAPE DESIGN
• -LOGO COLORS
• -NOT BUSY BUT CLEAN AND SHARP
• -MATTE COLORS
Nice to have
• Easy To read, Eye Catchy, Clean Design, logo colors, titles
Should not have
• not Busy,

```html
<!DOCTYPE html>
<html lang="en">
<head>
<meta charset="utf-8">
<title>Qr Lake Facades – New Roof Coming Soon Yard Sign</title>
<link href="https://fonts.googleapis.com/css2?family=Oswald:wght@200;300&family=Raleway:wght@400;500;700;800&display=swap" rel="stylesheet">
<style>
  :root{
    --teal:#219a89;
    --teal-light:#33b8a4;
    --dark:#333335;
    --mid-gray:#545457;
    --text-gray:#5c5c5c;
    --tagline-gray:#8a8a8c;
    --white:#ffffff;
    --page-bg:#155a52;
  }
  html,body{margin:0;padding:0;width:1200px;height:1200px;overflow:hidden;}
  body{background:radial-gradient(circle at 50% 45%, #1d7a6e 0%, var(--page-bg) 70%);}
  .yard-sign{position:absolute;left:211px;top:81px;width:778px;height:1038px;filter:drop-shadow(0 8px 18px rgba(0,0,0,.35));}
  .title-main{font-family:'Oswald',sans-serif;font-weight:200;fill:var(--teal-light);}
  .title-sub{font-family:'Raleway',sans-serif;font-weight:500;fill:var(--white);}
  .brand-name{font-family:'Raleway',sans-serif;font-weight:700;fill:var(--teal-light);}
  .brand-tagline{font-family:'Raleway',sans-serif;font-weight:500;fill:var(--tagline-gray);letter-spacing:1.5px;}
  .section-title{font-family:'Raleway',sans-serif;font-weight:800;fill:var(--teal);}
  .service-label{font-family:'Raleway',sans-serif;font-weight:500;font-size:15px;}
  .find-us{font-family:'Raleway',sans-serif;font-weight:500;fill:var(--dark);}
  .phone{font-family:'Oswald',sans-serif;font-weight:200;fill:var(--white);}
  .contact{font-family:'Raleway',sans-serif;font-weight:400;fill:var(--white);font-size:19px;}
</style>
</head>
<body>
<svg class="yard-sign" viewBox="0 0 648 865" xmlns="http://www.w3.org/2000/svg">
  <defs>
    <linearGradient id="roofPhoto" x1="0" y1="0" x2="0" y2="1"><stop offset="0" stop-color="#8a7a5a"/><stop offset="1" stop-color="#5b5650"/></linearGradient>
    <linearGradient id="gutterPhoto" x1="0" y1="0" x2="0" y2="1"><stop offset="0" stop-color="#cfd6dc"/><stop offset="1" stop-color="#6b4a32"/></linearGradient>
    <linearGradient id="paintPhoto" x1="0" y1="0" x2="1" y2="0"><stop offset="0" stop-color="#9aa0a4"/><stop offset="1" stop-color="#c9cbc6"/></linearGradient>
    <linearGradient id="sidingPhoto" x1="0" y1="0" x2="1" y2="1"><stop offset="0" stop-color="#b9c6d3"/><stop offset="1" stop-color="#9a4a3e"/></linearGradient>
    <linearGradient id="washPhoto" x1="0" y1="0" x2="0" y2="1"><stop offset="0" stop-color="#b79b44"/><stop offset="1" stop-color="#8f9190"/></linearGradient>
    <linearGradient id="atticPhoto" x1="0" y1="0" x2="1" y2="1"><stop offset="0" stop-color="#c8d5dc"/><stop offset="1" stop-color="#d9b86a"/></linearGradient>
  </defs>

  <!-- House silhouette -->
  <polygon class="roof-band" fill="var(--teal)" points="0,166 240,0 420,125 420,27 492,27 492,157 648,157 648,865 0,865"/>
  <polygon class="house-body" fill="var(--dark)" points="0,228 240,62 420,188 420,157 648,157 648,865 0,865"/>

  <!-- Middle panels -->
  <polygon class="gray-panel" fill="var(--mid-gray)" points="345,322 648,322 648,704 598,704 425,470 300,470"/>
  <polygon fill="var(--teal)" points="626,322 648,322 648,340"/>
  <polygon class="teal-panel" fill="var(--teal)" points="0,430 382,430 470,560 382,704 0,704"/>
  <polygon fill="var(--teal)" points="405,704 478,632 548,704"/>

  <!-- Brand -->
  <g class="brand">
    <rect x="118" y="178" width="58" height="58" fill="none" stroke="var(--teal-light)" stroke-width="5"/>
    <text class="brand-name" x="147" y="278" font-size="27" text-anchor="middle">QR LAKE</text>
    <text class="brand-name" x="147" y="312" font-size="27" text-anchor="middle">FACADES</text>
    <text class="brand-tagline" x="147" y="346" font-size="11" text-anchor="middle">SOLID WORK HONEST CARE</text>
  </g>

  <!-- Title -->
  <text class="title-main" x="292" y="248" font-size="100" textLength="330" lengthAdjust="spacingAndGlyphs">NEW ROOF</text>
  <line x1="292" y1="258" x2="622" y2="258" stroke="#555" stroke-width="1.5"/>
  <text class="title-sub" x="293" y="299" font-size="44" textLength="328" lengthAdjust="spacingAndGlyphs">COMING SOON</text>
  <line x1="292" y1="308" x2="622" y2="308" stroke="#555" stroke-width="1.5"/>

  <!-- Services -->
  <polygon class="services-band" fill="var(--white)" points="0,375 342,375 305,430 0,430"/>
  <text class="section-title" x="187" y="413" font-size="29" text-anchor="middle">SERVICES</text>

  <g class="service-list">
    <g class="service">
      <rect x="20" y="442" width="88" height="2" fill="var(--white)"/>
      <rect x="20" y="446" width="88" height="88" fill="url(#roofPhoto)" role="img" aria-label="Photo of roof shingles"/>
      <rect x="24" y="534" width="78" height="22" fill="var(--white)"/>
      <text class="service-label" x="63" y="550" text-anchor="middle" fill="var(--teal)">Roofing</text>
    </g>
    <g class="service">
      <rect x="124" y="442" width="88" height="2" fill="var(--white)"/>
      <rect x="124" y="446" width="88" height="88" fill="url(#gutterPhoto)" role="img" aria-label="Photo of a gutter downspout"/>
      <rect x="128" y="534" width="78" height="22" fill="var(--mid-gray)"/>
      <text class="service-label" x="167" y="550" text-anchor="middle" fill="var(--white)">Gutters</text>
    </g>
    <g class="service">
      <rect x="228" y="442" width="88" height="2" fill="var(--white)"/>
      <rect x="228" y="446" width="88" height="88" fill="url(#paintPhoto)" role="img" aria-label="Photo of a painter at work on a wall"/>
      <rect x="232" y="534" width="78" height="22" fill="var(--white)"/>
      <text class="service-label" x="271" y="550" text-anchor="middle" fill="var(--teal)">Painting</text>
    </g>
    <g class="service">
      <rect x="332" y="442" width="88" height="2" fill="var(--white)"/>
      <rect x="332" y="446" width="88" height="88" fill="url(#sidingPhoto)" role="img" aria-label="Photo of a worker installing siding"/>
      <rect x="336" y="534" width="78" height="22" fill="var(--mid-gray)"/>
      <text class="service-label" x="375" y="550" text-anchor="middle" fill="var(--white)">Siding</text>
    </g>
    <g class="service">
      <rect x="436" y="442" width="88" height="2" fill="var(--teal)"/>
      <rect x="436" y="446" width="88" height="88" fill="url(#washPhoto)" role="img" aria-label="Photo of pressure washing a driveway"/>
      <rect x="440" y="534" width="78" height="22" fill="var(--teal)"/>
      <text class="service-label" x="479" y="551" text-anchor="middle" fill="var(--white)">Pressure</text>
      <text class="service-label" x="479" y="572" text-anchor="middle" fill="var(--white)">Washing</text>
    </g>
    <g class="service">
      <rect x="540" y="442" width="88" height="2" fill="var(--white)"/>
      <rect x="540" y="446" width="88" height="88" fill="url(#atticPhoto)" role="img" aria-label="Photo of attic insulation work"/>
      <rect x="544" y="534" width="78" height="22" fill="var(--white)"/>
      <text class="service-label" x="583" y="551" text-anchor="middle" fill="var(--teal)">Attic</text>
      <text class="service-label" x="583" y="572" text-anchor="middle" fill="var(--teal-light)">Ventilation</text>
    </g>
  </g>

  <!-- Contact -->
  <line x1="24" y1="610" x2="88" y2="610" stroke="var(--dark)" stroke-width="2"/>
  <text class="find-us" x="200" y="619" font-size="26" text-anchor="middle">FIND US HERE</text>
  <line x1="312" y1="610" x2="378" y2="610" stroke="var(--dark)" stroke-width="2"/>
  <text class="phone" x="20" y="688" font-size="78" textLength="360" lengthAdjust="spacingAndGlyphs">555-210-4386</text>

  <g class="contact-line">
    <rect x="20" y="731" width="19" height="13" fill="none" stroke="var(--teal-light)" stroke-width="1.6"/>
    <polyline points="20,731 29.5,739 39,731" fill="none" stroke="var(--teal-light)" stroke-width="1.6"/>
    <text class="contact" x="44" y="743">: info@qrlakefacades.com</text>
    <circle cx="341" cy="738" r="8" fill="none" stroke="var(--teal-light)" stroke-width="1.6"/>
    <line x1="333" y1="738" x2="349" y2="738" stroke="var(--teal-light)" stroke-width="1.2"/>
    <ellipse cx="341" cy="738" rx="3.5" ry="8" fill="none" stroke="var(--teal-light)" stroke-width="1.2"/>
    <text class="contact" x="354" y="743">: www.qrlakefacades.com</text>
  </g>

  <g class="social-dots" fill="var(--teal)">
    <circle cx="128" cy="800" r="13"/>
    <circle cx="165" cy="800" r="13"/>
    <circle cx="202" cy="800" r="13"/>
    <circle cx="240" cy="800" r="13"/>
    <circle cx="277" cy="800" r="13"/>
    <circle cx="315" cy="800" r="13"/>
  </g>
  <line x1="355" y1="772" x2="355" y2="832" stroke="#555" stroke-width="1.5"/>
  <g class="credential-badges">
    <rect x="386" y="780" width="25" height="41" fill="var(--white)"/>
    <rect x="422" y="778" width="112" height="43" fill="#d8232a"/>
  </g>

  <rect class="base-bar" x="95" y="845" width="458" height="20" fill="var(--teal)"/>
</svg>
</body>
</html>
```